private relaxation massage therapist business card

I want a card that does not give a physical address as I am able to massage at home as well as be mobile. I want on the back somewhere to put appointment details and also my bank acct details for payment being to acct 38 6042 0071846 00
I have a Certificate in Relaxation Massage from KTRB 2014
I would like to use blue colours and maybe have some fluffy clouds somewhere on the business card.

Industry/Entity Type

Massage

Contact Information for Business Card

Megan Pollard
Relaxation Massage Therapist

telephone 0218 647 092 or 09 8416375
email meganpollard72@quillmail.com

Requirements
Must have
• bold lettering, lots of white space, On the reverse of the card some lines in a box for me to write appointment times also on reverse my bank acct details for payment on line.

```html
<!DOCTYPE html>
<html lang="en">
<head>
<meta charset="utf-8">
<title>Megan Pollard – Relaxation Massage Therapist – Business Card</title>
<link rel="stylesheet" href="https://fonts.googleapis.com/css2?family=Lexend:wght@600&family=Arimo:wght@400;500&display=swap">
<style>
  :root {
    --page-bg: #ffffff;
    --card-teal: #59bfcc;
    --card-ink: #ffffff;
    --card-line: rgba(255, 255, 255, 0.85);
    --card-shadow: rgba(0, 0, 0, 0.45);
  }
  * { margin: 0; padding: 0; box-sizing: border-box; }
  html, body {
    width: 1200px;
    height: 900px;
    overflow: hidden;
    background: var(--page-bg);
  }
  .sheet {
    position: relative;
    width: 1200px;
    height: 900px;
  }
  .card {
    position: absolute;
    background: var(--card-teal);
    color: var(--card-ink);
    box-shadow: 3px 3px 6px var(--card-shadow);
  }
  .card--front {
    left: 77px;
    top: 120px;
    width: 428px;
    height: 692px;
  }
  .card--back {
    left: 678px;
    top: 117px;
    width: 429px;
    height: 695px;
  }
  .card__name {
    position: absolute;
    left: 38px;
    top: 526px;
    font-family: "Lexend", "Century Gothic", sans-serif;
    font-weight: 600;
    font-size: 35px;
    letter-spacing: 0.2px;
    line-height: 1.1;
  }
  .card__role {
    position: absolute;
    left: 38px;
    top: 584px;
    font-family: "Arimo", Arial, sans-serif;
    font-weight: 500;
    font-size: 14.5px;
    letter-spacing: 0.8px;
    line-height: 1;
  }
  .card__certificate {
    position: absolute;
    left: 38px;
    top: 610px;
    font-family: "Arimo", Arial, sans-serif;
    font-size: 12px;
    letter-spacing: 0.5px;
    line-height: 1;
  }
  .appointments {
    position: absolute;
    left: 23px;
    top: 40px;
    width: 383px;
    border: 1.5px solid var(--card-line);
    padding: 16px 18px 22px;
    font-family: "Arimo", Arial, sans-serif;
  }
  .appointments__title {
    font-size: 16px;
    font-weight: 500;
    letter-spacing: 0.8px;
    margin-bottom: 6px;
  }
  .appointments__line {
    height: 38px;
    border-bottom: 1px solid var(--card-line);
  }
  .contact {
    position: absolute;
    left: 23px;
    top: 559px;
    font-family: "Arimo", Arial, sans-serif;
    font-weight: 500;
    line-height: 1;
  }
  .contact__phone {
    font-size: 21.5px;
    letter-spacing: 0.3px;
  }
  .contact__email,
  .contact__account {
    font-size: 16px;
    letter-spacing: 0.4px;
  }
  .contact__email { margin-top: 14px; }
  .contact__account { margin-top: 21px; }
</style>
</head>
<body>
  <main class="sheet">
    <section class="card card--front" aria-label="Card front">
      <h1 class="card__name">Megan Pollard</h1>
      <p class="card__role">Relaxation Massage Therapist</p>
      <p class="card__certificate">Certificate in Relaxation Massage – KTRB 2014</p>
    </section>

    <section class="card card--back" aria-label="Card back">
      <div class="appointments">
        <p class="appointments__title">Appointments</p>
        <div class="appointments__line"></div>
        <div class="appointments__line"></div>
        <div class="appointments__line"></div>
        <div class="appointments__line"></div>
        <div class="appointments__line"></div>
        <div class="appointments__line"></div>
        <div class="appointments__line"></div>
      </div>
      <div class="contact">
        <p class="contact__phone">Ph: 0218 647 092,09 8416375</p>
        <p class="contact__email">mail: meganpollard72@quillmail.com</p>
        <p class="contact__account">acct 38 6042 0071846 00</p>
      </div>
    </section>
  </main>
</body>
</html>
```